Mobile App design improvement- (plain square)

I have four screens need to redesign, and I have the design guide to help you.
The goal is to make the design clean and easy to understand CTA improve UI/UX. You can change the icons, and don't change the fonts or color. Also, if you are doing a great job, I will hire you finish the rest of the design of the app.
Here is our site: https://pelvosta.com
Pelvosta App is wishlist:
Hight features and app propositions of the app collaborative shopping and chatting with invited friends and family. Easily to get feedback and make decisions of the products from friends, chat, vote, poll, compare.
Here is the (plain square) link: https://www.example-design.com/design/Kx7Tq2LmWz9PbNv4HdYsRe/Pelvosta--App?node-id=31-47215&t=Jq8WmZr3VxNt5KpLa-7
Here is the app links:
IOS app:
https://lnkhop.io/8KqTz2m

Android app:
https://lnkhop.io/8KqTz2p
Updates

1. I need to have more design ideas that makes users feel simple and easy to understudy platforms can add products from search products, paste url, and use share button to add proton there wishlist from other e-commerce sites. Simplify the search, paste url, and user share button page, maybe combine search with paste url in the search bar, or switch back and forth with search key, paste URL, or share product from other e-commerce sites. Shop page, maybe show users to pick favorites brands recommended products and popular brands. My profile page, I need to be simple but also give users ability to navigate between the save money and wishlists. Please don’t change my color of the app header and color theme. Tone: Ecommerce marketplace, social media, fun! Highlights invite friends chat, save money, and add product.

Trendra Market(s)

female CEOs, moms, female interns

Industry/Entity Type

Social networking, shopping.

Number of Pages Required

4 page

Font styles to use
Other font styles liked:
• please look at our brand guide

Requirements
Nice to have
• Simple design, highlight invite memebers, and highlight 3 options for them to get products into one place. Highlight collabrative and social tone.
Should not have
• Don't give me too much colors.

```html
<!DOCTYPE html>
<html lang="en">
<head>
<meta charset="utf-8">
<title>Pelvosta Redesign Screen Apps</title>
<link href="https://fonts.googleapis.com/css2?family=Outfit:wght@300;400;500;600;700&display=swap" rel="stylesheet">
<style>
:root{
  --primary:#E4F7D2;
  --primary-soft:#F3FBEC;
  --secondary:#4437C9;
  --secondary-light:#7D73DF;
  --secondary-pale:#EAE8FB;
  --tertiary:#FDD447;
  --quarter:#3E3A37;
  --stage:#A9A9A9;
  --ink:#26252E;
  --muted:#7B7A86;
  --line:#D8D5F3;
  --chip-text:#9088E2;
  --teal:#52D5C6;
  --pink:#E85BA8;
  --white:#FFFFFF;
}
*{box-sizing:border-box;margin:0;padding:0}
html,body{width:872px;height:1200px;overflow:hidden;background:var(--stage)}
body{font-family:"Outfit",sans-serif;color:var(--ink)}
.stage{position:absolute;left:0;top:0;width:1648px;height:2268px;background:var(--stage);transform:scale(0.52913);transform-origin:0 0}
.abs{position:absolute}
svg.ic{width:18px;height:18px;fill:none;stroke:currentColor;stroke-width:1.8;stroke-linecap:round;stroke-linejoin:round}

/* banner + legend */
.banner{position:absolute;left:0;top:0;width:1648px;height:85px;background:var(--secondary);color:var(--white);font-size:44px;font-weight:600;text-align:center;line-height:88px;letter-spacing:.2px}
.legend{position:absolute;left:52px;top:123px;display:flex;align-items:center;height:44px;font-size:23px;font-weight:500;color:var(--quarter)}
.swatch{width:44px;height:44px;margin-right:14px}
.legend .lbl{margin-right:16px}
.legend .mark{width:28px;height:28px;border-radius:6px;background:var(--quarter);margin:0 24px 0 4px}

/* phone shell */
.phone{position:absolute;width:365px;border-radius:40px;overflow:hidden;background:var(--secondary)}
.phone.yellow{background:var(--tertiary)}
.status{position:absolute;left:38px;right:38px;top:16px;display:flex;justify-content:space-between;align-items:center;color:var(--white);font-size:13px;font-weight:500}
.phone.yellow .status{color:var(--quarter)}
.status .sys{display:flex;gap:10px;align-items:center}
.sheet{position:absolute;left:0;right:0;top:60px;bottom:0;border-radius:34px 34px 0 0;background:var(--white)}
.sheet::before{content:"";position:absolute;left:34px;right:34px;top:-8px;height:22px;background:var(--secondary-light);border-radius:50% 50% 0 0/100% 100% 0 0;z-index:-1}
.sheet.green{background:linear-gradient(180deg,var(--primary-soft) 0%,var(--primary) 100%)}
.topbar{position:absolute;left:0;right:0;top:84px;height:32px}
.topbar .title{position:absolute;top:6px;font-size:15px;font-weight:500;color:var(--ink)}
.round{position:absolute;top:0;width:32px;height:32px;border-radius:50%;border:1px solid var(--line);background:var(--white);display:flex;align-items:center;justify-content:center;color:var(--secondary)}
.hr{position:absolute;left:0;right:0;height:1px;background:#E4E2EE}
.band{position:absolute;left:0;right:0;height:3px;background:#E4E2EE}

/* tab bar */
.tabbar{position:absolute;left:0;right:0;height:72px;background:var(--white);display:flex;border-top:1px solid #EEE}
.tab{flex:1;display:flex;flex-direction:column;align-items:center;justify-content:center;gap:4px;font-size:10px;color:#B0ACD8}
.tab svg{width:22px;height:22px;fill:#C9C5EE;stroke:none}
.tab.active{color:var(--secondary);border-top:4px solid var(--secondary);background:var(--secondary-pale)}
.tab.active svg{fill:var(--secondary)}

/* form bits */
.label{position:absolute;left:21px;font-size:14px;font-weight:500}
.field{position:absolute;left:21px;width:323px;height:48px;border:1px solid var(--line);border-radius:6px;background:var(--white);font-size:12px;font-style:italic;color:#55535E;padding:16px 10px}
.search{position:absolute;left:21px;width:323px;height:40px;border:1.5px solid var(--secondary);border-radius:8px;background:var(--white);display:flex;align-items:center;justify-content:space-between;padding:0 16px;font-size:14px;color:#A7A5B4}
.search svg{color:#55535E}
.btn{position:absolute;background:var(--secondary);color:var(--white);border-radius:6px;font-size:14px;font-weight:500;display:flex;align-items:center;justify-content:center;gap:10px}
.seg{position:absolute;left:21px;width:323px;height:50px;border:1px solid var(--line);border-radius:8px;background:var(--white);display:flex;padding:4px;gap:4px;font-size:14px}
.seg span{flex:1;display:flex;align-items:center;justify-content:center;border-radius:6px;color:#A7A2E8}
.seg span.on{background:var(--secondary-pale);color:var(--secondary);font-weight:500}
.hint{position:absolute;left:21px;width:323px;height:42px;border-radius:8px;background:var(--tertiary);display:flex;align-items:center;padding:0 12px;gap:8px;font-size:13px;color:var(--quarter)}
.hint u{color:var(--secondary);font-style:italic}
.hint .x{margin-left:auto;color:var(--secondary)}
.link{color:var(--secondary)}

/* photo fills */
.ph{position:absolute;overflow:hidden}
.ph-blue{background:linear-gradient(150deg,#3A86E0,#2160C7)}
.ph-white{background:linear-gradient(180deg,#F4F4F4,#DADADA)}
.ph-dark{background:linear-gradient(160deg,#2F3538,#3C6CC9)}
.ph-steel{background:linear-gradient(160deg,#5D7FD6,#3C5FB8)}
.ph-tan{background:linear-gradient(160deg,#C9B79A,#8C6E4E)}
.ph-black{background:linear-gradient(160deg,#E8E2D8,#1C1C1E 60%)}
.ph-sky{background:linear-gradient(160deg,#7EC6F2,#F2D68A)}
.ph-face{background:linear-gradient(160deg,#B07A4C,#6A3E22)}
.ph-grey{background:linear-gradient(160deg,#D5D5D5,#8C8C8C)}

/* product cards */
.off{position:absolute;top:8px;right:8px;height:12px;padding:0 5px;border-radius:6px;background:#C9C5EE;color:var(--white);font-size:7px;line-height:12px}
.check{position:absolute;top:8px;left:8px;width:12px;height:12px;border-radius:3px;background:var(--white);border:1px solid #CCC}
.pname{font-size:14px;font-weight:600;color:var(--ink)}
.rate{font-size:10px;color:var(--ink);display:flex;gap:6px;align-items:center}
.rate b{color:var(--tertiary);font-weight:400}
.brand{font-size:12px;font-weight:700;color:var(--ink)}
.price{font-size:22px;font-weight:500;color:var(--ink)}
.price small{font-size:9px;color:#9E9CA8;text-decoration:line-through;margin-left:6px}
.acts{display:flex;gap:8px}
.cmp{height:24px;padding:0 8px;border:1px solid var(--secondary);border-radius:4px;color:var(--secondary);font-size:12px;display:flex;align-items:center}
.add{height:24px;padding:0 8px;border-radius:4px;background:var(--secondary);color:var(--white);font-size:12px;display:flex;align-items:center;gap:8px}
.hcard{position:absolute;left:22px;width:320px;height:166px;border:1px solid #E6E4EF;border-radius:6px;overflow:hidden;background:var(--white)}
.hcard .ph{left:0;top:0;width:166px;height:166px}
.hcard .info{position:absolute;left:174px;top:6px;right:6px;bottom:8px}
.vcard{position:absolute;width:154px;height:302px;border:1px solid #E6E4EF;border-radius:6px;overflow:hidden;background:var(--white)}
.vcard .ph{left:0;top:0;width:154px;height:155px}
.vcard .info{position:absolute;left:8px;right:6px;top:160px}

/* chips & retailers */
.chips{position:absolute;left:21px;display:flex;gap:8px}
.chip{height:28px;padding:0 14px;border:1px solid #E2DFF6;border-radius:14px;background:var(--primary-soft);color:var(--chip-text);font-size:14px;display:flex;align-items:center}
.chip.more{background:var(--secondary);color:var(--white);border-color:var(--secondary);padding:0 14px;font-weight:700}
.retail{position:absolute;left:22px;top:437px;width:323px;height:230px;border-radius:14px;background:var(--teal)}
.tile{position:absolute;width:62px;text-align:center;font-size:14px;color:var(--quarter)}
.tile i{display:flex;width:62px;height:62px;border-radius:12px;background:#F3F6F6;margin-bottom:6px;align-items:center;justify-content:center}
.tile i em{width:28px;height:28px;border-radius:50%;background:var(--quarter);display:block}
</style>
</head>
<body>
<svg width="0" height="0" style="position:absolute">
  <defs>
    <symbol id="i-bell" viewBox="0 0 24 24"><path d="M6 16V11a6 6 0 0 1 12 0v5l1.5 2h-15z"/><path d="M10 20a2 2 0 0 0 4 0"/></symbol>
    <symbol id="i-gear" viewBox="0 0 24 24"><circle cx="12" cy="12" r="3"/><path d="M12 3l2 2.5 3-.5 1 3 2.5 1.5-1 3 1 3-2.5 1.5-1 3-3-.5L12 21l-2-2.5-3 .5-1-3L3.5 14.5l1-2.5-1-3L6 7.5l1-3 3 .5z"/></symbol>
    <symbol id="i-back" viewBox="0 0 24 24"><path d="M15 5l-7 7 7 7"/></symbol>
    <symbol id="i-next" viewBox="0 0 24 24"><path d="M9 5l7 7-7 7"/></symbol>
    <symbol id="i-down" viewBox="0 0 24 24"><path d="M6 9l6 6 6-6"/></symbol>
    <symbol id="i-search" viewBox="0 0 24 24"><circle cx="11" cy="11" r="7"/><path d="M16.5 16.5L21 21"/></symbol>
    <symbol id="i-plus" viewBox="0 0 24 24"><path d="M12 5v14M5 12h14"/></symbol>
    <symbol id="i-plusc" viewBox="0 0 24 24"><circle cx="12" cy="12" r="9"/><path d="M12 8v8M8 12h8"/></symbol>
    <symbol id="i-help" viewBox="0 0 24 24"><circle cx="12" cy="12" r="9"/><path d="M9.5 9.5a2.5 2.5 0 1 1 3.5 2.3c-.7.3-1 .8-1 1.5"/><path d="M12 16.5v.5"/></symbol>
    <symbol id="i-pin" viewBox="0 0 24 24"><path d="M12 21s-6-6-6-11a6 6 0 0 1 12 0c0 5-6 11-6 11z"/><circle cx="12" cy="10" r="2"/></symbol>
    <symbol id="i-edit" viewBox="0 0 24 24"><path d="M4 20l4-1 11-11-3-3L5 16z"/></symbol>
    <symbol id="i-filter" viewBox="0 0 24 24"><path d="M4 6h16M4 12h16M4 18h16"/><circle cx="9" cy="6" r="1.5"/><circle cx="15" cy="12" r="1.5"/><circle cx="8" cy="18" r="1.5"/></symbol>
    <symbol id="i-tag" viewBox="0 0 24 24"><path d="M3 12l9-9h7v7l-9 9z"/><circle cx="15.5" cy="7.5" r="1.3"/></symbol>
    <symbol id="i-ticket" viewBox="0 0 24 24"><path d="M4 7h16v3a2 2 0 0 0 0 4v3H4v-3a2 2 0 0 0 0-4z"/><path d="M10 8v8"/></symbol>
    <symbol id="i-cash" viewBox="0 0 24 24"><rect x="3" y="6" width="18" height="12" rx="2"/><circle cx="12" cy="12" r="3"/></symbol>
    <symbol id="n-home" viewBox="0 0 24 24"><path d="M4 10l8-6 8 6v10H4z"/></symbol>
    <symbol id="n-globe" viewBox="0 0 24 24"><path d="M12 3a9 9 0 1 1 0 18 9 9 0 0 1 0-18zm-3 5c2 1 1 3 3 4s1 4 3 5c2-2 3-5 1-7-2 0-3-2-7-2z"/></symbol>
    <symbol id="n-add" viewBox="0 0 24 24"><path d="M5 3h14a2 2 0 0 1 2 2v14a2 2 0 0 1-2 2H5a2 2 0 0 1-2-2V5a2 2 0 0 1 2-2zm1 2v14h12V5zm5 3h2v3h3v2h-3v3h-2v-3H8v-2h3z"/></symbol>
    <symbol id="n-chat" viewBox="0 0 24 24"><path d="M3 4h13v10H8l-5 4zm15 4h3v12l-4-3h-8v-1h9z"/></symbol>
    <symbol id="n-bag" viewBox="0 0 24 24"><path d="M5 6h14l-1 15H6zm4 2a3 3 0 0 0 6 0h-1.5a1.5 1.5 0 0 1-3 0z"/></symbol>
    <symbol id="s-wifi" viewBox="0 0 24 16"><path d="M12 14l3-3a4 4 0 0 0-6 0zm-6-6l2 2a6 6 0 0 1 8 0l2-2a9 9 0 0 0-12 0zM2 4l2 2a11 11 0 0 1 16 0l2-2A14 14 0 0 0 2 4z"/></symbol>
    <symbol id="s-sig" viewBox="0 0 20 14"><path d="M1 10h3v4H1zm5-3h3v7H6zm5-3h3v10h-3zm5-4h3v14h-3z"/></symbol>
    <symbol id="s-bat" viewBox="0 0 26 14"><rect x="1" y="1" width="21" height="12" rx="3" fill="none" stroke="currentColor" stroke-width="1.5"/><rect x="3" y="3" width="17" height="8" rx="1.5"/><rect x="23" y="5" width="2" height="4"/></symbol>
  </defs>
</svg>

<main class="stage">
  <header class="banner">Pelvosta Redesign Screen Apps</header>
  <div class="legend">
    <span class="swatch" style="background:var(--primary)"></span><span class="lbl">Primary</span>
    <span class="swatch" style="background:var(--secondary)"></span><span class="lbl">Secondary</span>
    <span class="swatch" style="background:var(--tertiary)"></span><span class="lbl">Tertiary</span>
    <span class="swatch" style="background:var(--quarter)"></span><span class="lbl">Quarter</span>
    <span class="mark"></span><span>Https://Lnkhop.Io/R7vqn</span>
  </div>

  <!-- ========== MY PROFILE ========== -->
  <section class="phone" style="left:52px;top:205px;height:792px">
    <div class="status"><span>09:45</span><span class="sys"><svg width="20" height="14" fill="currentColor"><use href="#s-wifi"/></svg><svg width="18" height="13" fill="currentColor"><use href="#s-sig"/></svg><svg width="24" height="14" fill="currentColor"><use href="#s-bat"/></svg></span></div>
    <div class="sheet green"></div>
    <div class="topbar">
      <span class="title" style="left:21px">My Profile</span>
      <span class="round" style="right:60px"><svg class="ic"><use href="#i-bell"/></svg></span>
      <span class="round" style="right:20px"><svg class="ic"><use href="#i-gear"/></svg></span>
    </div>
    <div class="hr" style="top:127px"></div>

    <div class="abs" style="left:21px;top:140px;width:86px;height:86px;border-radius:50%;border:2px dashed var(--secondary);padding:5px">
      <div class="ph ph-face" style="position:relative;width:100%;height:100%;border-radius:50%" role="img" aria-label="Profile photo of the user"></div>
      <span class="abs" style="right:4px;bottom:2px;width:16px;height:16px;border-radius:50%;background:#4CC23A;border:2px solid var(--white)"></span>
    </div>
    <div class="abs" style="left:120px;top:146px;font-size:15px;font-weight:500;display:flex;gap:8px;align-items:center">Marisol Tendeka <svg class="ic" style="width:14px;height:14px;color:var(--secondary-light)"><use href="#i-edit"/></svg></div>
    <div class="abs" style="left:120px;top:164px;font-size:10px;line-height:13px">@marisol97<br><span style="display:inline-flex;gap:4px;align-items:center">Indonesia <svg class="ic" style="width:11px;height:11px;color:var(--secondary)"><use href="#i-pin"/></svg></span></div>
    <div class="abs" style="left:120px;top:206px;font-size:11px">1 Wishlist &nbsp;|&nbsp; Members</div>

    <div class="abs" style="left:21px;top:238px;width:323px;height:217px;border:1px solid var(--line);border-radius:14px;background:var(--white);padding:0 20px">
      <div style="display:flex;align-items:center;height:70px;border-bottom:1px solid var(--line);gap:12px">
        <svg class="ic" style="width:24px;height:24px;color:var(--secondary-light)"><use href="#i-tag"/></svg>
        <div style="flex:1"><div class="link" style="font-size:14px">Price drop</div><div style="font-size:12px;color:#55535E;line-height:15px">Get notified when your favorite<br>items go on sale.</div></div>
        <svg class="ic" style="width:22px;height:22px;color:var(--secondary)"><use href="#i-next"/></svg>
      </div>
      <div style="display:flex;align-items:center;height:70px;border-bottom:1px solid var(--line);gap:12px">
        <svg class="ic" style="width:24px;height:24px;color:var(--secondary-light)"><use href="#i-ticket"/></svg>
        <div style="flex:1"><div class="link" style="font-size:14px">Coupon</div><div style="font-size:12px;color:#55535E;line-height:15px">Discover and apply coupons to save<br>more instantly.</div></div>
        <svg class="ic" style="width:22px;height:22px;color:var(--secondary)"><use href="#i-next"/></svg>
      </div>
      <div style="display:flex;align-items:center;height:70px;gap:12px">
        <svg class="ic" style="width:24px;height:24px;color:var(--secondary-light)"><use href="#i-cash"/></svg>
        <div style="flex:1"><div class="link" style="font-size:14px">Cash Back</div><div style="font-size:12px;color:#55535E;line-height:15px">Earn money back on every eligible<br>purchase.</div></div>
        <svg class="ic" style="width:22px;height:22px;color:var(--secondary)"><use href="#i-next"/></svg>
      </div>
    </div>

    <div class="seg" style="top:470px;height:48px"><span class="on" style="background:var(--secondary);color:var(--white);font-weight:400">My Wishlist</span><span style="color:var(--secondary)">Joined Wishlist</span></div>

    <div class="abs" style="left:21px;top:532px;width:323px;height:152px;border:1.5px dashed var(--secondary);border-radius:4px;background:var(--white);display:flex;flex-direction:column;align-items:center;justify-content:center;gap:2px;color:var(--secondary);font-size:14px">
      <svg class="ic" style="width:22px;height:22px"><use href="#i-plusc"/></svg>Add Wishlist
    </div>

    <nav class="tabbar" style="top:720px">
      <span class="tab"><svg><use href="#n-home"/></svg>Home</span>
      <span class="tab"><svg><use href="#n-globe"/></svg>Discover</span>
      <span class="tab"><svg><use href="#n-add"/></svg>Wishlist</span>
      <span class="tab"><svg><use href="#n-chat"/></svg>Chat</span>
      <span class="tab active"><svg><use href="#n-bag"/></svg>Shop</span>
    </nav>
  </section>

  <!-- ========== 3 WAYS ========== -->
  <section class="phone yellow" style="left:445px;top:205px;height:792px">
    <div class="status"><span>09:45</span><span class="sys"><svg width="20" height="14" fill="currentColor"><use href="#s-wifi"/></svg><svg width="18" height="13" fill="currentColor"><use href="#s-sig"/></svg><svg width="24" height="14" fill="currentColor"><use href="#s-bat"/></svg></span></div>
    <div class="sheet"></div>
    <div class="topbar">
      <span class="round" style="left:21px"><svg class="ic"><use href="#i-back"/></svg></span>
      <span class="title" style="left:70px">3 Ways to find the products</span>
      <span class="round" style="right:60px"><svg class="ic"><use href="#i-bell"/></svg></span>
      <span class="round" style="right:20px"><svg class="ic"><use href="#i-gear"/></svg></span>
    </div>
    <div class="hr" style="top:127px"></div>

    <div class="abs" style="left:21px;top:140px;width:323px;height:128px;border:1px solid #D8D8DE;border-radius:8px;background:#F7F7F9;text-align:center">
      <div style="font-size:40px;font-weight:700;color:var(--secondary);line-height:44px;margin-top:4px">1</div>
      <div style="font-size:12px;line-height:15px;margin-top:2px">Quickly find what you're looking for by typing the<br>product name or keyword.</div>
      <div class="abs" style="left:20px;top:84px;width:282px;height:40px;border:1.5px solid var(--secondary);border-radius:6px;background:var(--white)">
        <span class="abs" style="left:6px;top:2px;height:34px;padding:0 8px;border:2px solid var(--pink);border-radius:12px;font-size:12px;line-height:30px;color:#55535E">Name of products</span>
        <svg class="ic abs" style="right:16px;top:10px;width:16px;height:16px;color:#55535E"><use href="#i-search"/></svg>
      </div>
    </div>

    <div class="abs" style="left:21px;top:276px;width:323px;height:128px;border:1px solid #D8D8DE;border-radius:8px;background:#F7F7F9;text-align:center">
      <div style="font-size:40px;font-weight:700;color:var(--secondary);line-height:44px;margin-top:4px">2</div>
      <div style="font-size:12px;line-height:15px;margin-top:2px">Already found something you like? Just paste the<br>product link to add it to your wishlist.</div>
      <div class="abs" style="left:100px;top:80px;width:203px;height:40px;border-bottom:1.5px solid var(--secondary);background:var(--white)">
        <span class="abs" style="left:2px;top:0;height:40px;padding:0 12px;border:2px solid var(--pink);border-radius:12px;font-size:14px;line-height:36px;color:#A7A5B4">https://</span>
      </div>
    </div>

    <div class="abs" style="left:21px;top:412px;width:323px;height:238px;border:1px solid #D8D8DE;border-radius:8px;background:#F7F7F9;text-align:center">
      <div style="font-size:40px;font-weight:700;color:var(--secondary);line-height:44px;margin-top:4px">3</div>
      <div style="font-size:12px;line-height:15px;margin-top:2px">Use the share feature from any shopping app to<br>instantly save the product here.</div>
      <div class="ph ph-white" style="left:58px;top:90px;width:80px;height:88px" role="img" aria-label="Phone screen of a shopping app with a sneaker and its share button"></div>
      <span class="abs" style="left:126px;top:162px;width:18px;height:18px;border:1.5px solid var(--pink);border-radius:50%"></span>
      <svg class="abs" style="left:148px;top:144px" width="28" height="12" viewBox="0 0 28 12"><path d="M1 6h24M20 1l5 5-5 5" fill="none" stroke="var(--pink)" stroke-width="1.8"/></svg>
      <div class="ph ph-black" style="left:180px;top:90px;width:82px;height:112px" role="img" aria-label="Share sheet showing the app as a destination"></div>
      <div class="abs" style="left:58px;top:208px;font-size:9px;line-height:11px;text-align:left;color:#55535E">Klik share button on<br>ecommerce apps</div>
      <div class="abs" style="left:180px;top:208px;font-size:9px;line-height:11px;text-align:left;color:#55535E">Choose Pelvosta<br>apps as destination</div>
    </div>

    <div class="btn" style="left:127px;top:665px;width:111px;height:40px">Find Product</div>

    <nav class="tabbar" style="top:720px">
      <span class="tab"><svg><use href="#n-home"/></svg>Home</span>
      <span class="tab"><svg><use href="#n-globe"/></svg>Discover</span>
      <span class="tab"><svg><use href="#n-add"/></svg>Wishlist</span>
      <span class="tab"><svg><use href="#n-chat"/></svg>Chat</span>
      <span class="tab active"><svg><use href="#n-bag"/></svg>Shop</span>
    </nav>
  </section>

  <!-- ========== NEW WISHLIST ========== -->
  <section class="phone" style="left:838px;top:205px;height:2031px">
    <div class="status"><span>09:45</span><span class="sys"><svg width="20" height="14" fill="currentColor"><use href="#s-wifi"/></svg><svg width="18" height="13" fill="currentColor"><use href="#s-sig"/></svg><svg width="24" height="14" fill="currentColor"><use href="#s-bat"/></svg></span></div>
    <div class="sheet"></div>
    <div class="topbar">
      <span class="round" style="left:21px"><svg class="ic"><use href="#i-back"/></svg></span>
      <span class="title" style="left:0;right:0;text-align:center">New Wishlist</span>
      <span class="round" style="right:60px"><svg class="ic"><use href="#i-bell"/></svg></span>
      <span class="round" style="right:20px"><svg class="ic"><use href="#i-gear"/></svg></span>
    </div>
    <div class="hr" style="top:127px"></div>

    <span class="label" style="top:140px">Title</span>
    <div class="field" style="top:160px">Your wishlist title</div>
    <span class="label" style="top:216px">Date</span>
    <div class="field" style="top:237px">DD/MM/YYYY</div>
    <span class="label" style="top:293px">Address</span>
    <div class="field" style="top:313px">Street address, city, zip code</div>
    <span class="label" style="top:369px">Descriptions (optional)</span>
    <div class="field" style="top:390px;height:85px;padding-top:12px">Details of the event or requrement</div>
    <div class="btn" style="left:21px;top:488px;width:154px;height:40px">Open chat</div>
    <div class="band" style="top:547px"></div>

    <span class="label" style="top:575px">Products (4)</span>
    <span class="abs link" style="right:21px;top:577px;font-size:13px">$257.00</span>
    <div class="abs" style="left:21px;top:604px;width:140px;height:64px;border-radius:8px;overflow:hidden;display:flex">
      <div class="ph-blue" style="flex:1" role="img" aria-label="Yellow sneaker thumbnail"></div>
      <div class="ph-white" style="flex:1" role="img" aria-label="High top sneaker thumbnail"></div>
      <div class="ph-steel" style="flex:1.4" role="img" aria-label="Headphones thumbnail"></div>
    </div>
    <div class="search" style="top:683px">https://<svg class="ic"><use href="#i-search"/></svg></div>
    <div class="seg" style="top:734px"><span>Enter Keyword</span><span class="on">Paste Link</span></div>
    <div class="hint" style="top:790px"><svg class="ic" style="width:18px;height:18px"><use href="#i-help"/></svg>3 Ways to find the products. <u>Learn more</u><span class="x">✕</span></div>
    <div class="btn" style="left:21px;top:841px;width:86px;height:38px">Add <svg class="ic"><use href="#i-plus"/></svg></div>
    <div class="band" style="top:899px"></div>

    <span class="label" style="top:928px">Members (1)</span>
    <span class="abs link" style="right:32px;top:930px;font-size:12px">View All</span>
    <div class="abs" style="left:21px;top:958px;width:64px;height:64px;border-radius:50%;border:1.5px solid var(--secondary);padding:2px">
      <div class="ph ph-grey" style="position:relative;width:100%;height:100%;border-radius:50%" role="img" aria-label="Member profile photo"></div>
    </div>
    <span class="abs" style="left:24px;top:1029px;font-size:14px">Dr. Halden</span>
    <div class="search" style="top:1059px">Username<svg class="ic"><use href="#i-search"/></svg></div>
    <div class="btn" style="left:21px;top:1107px;width:86px;height:38px">Invite <svg class="ic"><use href="#i-plus"/></svg></div>
    <div class="band" style="top:1166px"></div>

    <span class="label" style="top:1194px;left:23px">Suggested (207)</span>
    <span class="abs link" style="right:22px;top:1193px;font-size:16px">See all</span>

    <div class="hcard" style="top:1220px">
      <div class="ph ph-blue" role="img" aria-label="Yellow low sneaker product photo"><span class="check"></span><span class="off">50% OFF</span></div>
      <div class="info"><div class="pname">Yellow low sneakers</div><div class="rate"><b>★</b>4.8 <span>• 1028 sold</span></div>
        <div class="brand" style="margin-top:32px">ambrola</div><div class="price">$37.50<small>$75.00</small></div>
        <div class="acts" style="margin-top:12px"><span class="cmp">Compare</span><span class="add">Add <svg class="ic" style="width:14px;height:14px"><use href="#i-plus"/></svg></span></div></div>
    </div>
    <div class="hcard" style="top:1394px">
      <div class="ph ph-tan" role="img" aria-label="Canvas tote bag product photo"><span class="check"></span><span class="off">50% OFF</span></div>
      <div class="info"><div class="pname">Yellow low sneakers</div><div class="rate"><b>★</b>4.8 <span>• 1028 sold</span></div>
        <div class="brand" style="margin-top:32px">ambrola</div><div class="price">$37.50<small>$75.00</small></div>
        <div class="acts" style="margin-top:12px"><span class="cmp">Compare</span><span class="add">Add <svg class="ic" style="width:14px;height:14px"><use href="#i-plus"/></svg></span></div></div>
    </div>
    <div class="hcard" style="top:1568px">
      <div class="ph ph-black" role="img" aria-label="Black printed t-shirt on a hanger"><span class="check"></span><span class="off">50% OFF</span></div>
      <div class="info"><div class="pname">Yellow low sneakers</div><div class="rate"><b>★</b>4.8 <span>• 1028 sold</span></div>
        <div class="brand" style="margin-top:32px">ambrola</div><div class="price">$37.50<small>$75.00</small></div>
        <div class="acts" style="margin-top:12px"><span class="cmp">Compare</span><span class="add">Add <svg class="ic" style="width:14px;height:14px"><use href="#i-plus"/></svg></span></div></div>
    </div>
    <div class="hcard" style="top:1742px">
      <div class="ph ph-sky" role="img" aria-label="Yellow hoodie product photo"><span class="check"></span><span class="off">50% OFF</span></div>
      <div class="info"><div class="pname">Yellow low sneakers</div><div class="rate"><b>★</b>4.8 <span>• 1028 sold</span></div>
        <div class="brand" style="margin-top:32px">ambrola</div><div class="price">$37.50<small>$75.00</small></div>
        <div class="acts" style="margin-top:12px"><span class="cmp">Compare</span><span class="add">Add <svg class="ic" style="width:14px;height:14px"><use href="#i-plus"/></svg></span></div></div>
    </div>
    <span class="abs link" style="left:0;right:0;top:1918px;text-align:center;font-size:16px">See all</span>

    <nav class="tabbar" style="top:1959px">
      <span class="tab"><svg><use href="#n-home"/></svg>Home</span>
      <span class="tab"><svg><use href="#n-globe"/></svg>Discover</span>
      <span class="tab"><svg><use href="#n-add"/></svg>Wishlist</span>
      <span class="tab"><svg><use href="#n-chat"/></svg>Chat</span>
      <span class="tab active"><svg><use href="#n-bag"/></svg>Shop</span>
    </nav>
  </section>

  <!-- ========== SHOP ========== -->
  <section class="phone" style="left:1232px;top:205px;height:1538px">
    <div class="status"><span>09:45</span><span class="sys"><svg width="20" height="14" fill="currentColor"><use href="#s-wifi"/></svg><svg width="18" height="13" fill="currentColor"><use href="#s-sig"/></svg><svg width="24" height="14" fill="currentColor"><use href="#s-bat"/></svg></span></div>
    <div class="sheet green"></div>
    <div class="topbar">
      <span class="ph ph-face" style="left:21px;top:0;width:32px;height:32px;border-radius:50%" role="img" aria-label="User avatar"></span>
      <span class="title" style="left:0;right:0;text-align:center">Shop</span>
      <span class="round" style="right:60px"><svg class="ic"><use href="#i-bell"/></svg></span>
      <span class="round" style="right:20px"><svg class="ic"><use href="#i-gear"/></svg></span>
    </div>
    <div class="hr" style="top:127px"></div>

    <div class="search" style="top:140px">Name of products<svg class="ic"><use href="#i-search"/></svg></div>
    <div class="seg" style="top:191px;height:48px"><span class="on">Enter Keyword</span><span>Paste Link</span></div>
    <div class="hint" style="top:247px;height:40px"><svg class="ic" style="width:18px;height:18px"><use href="#i-help"/></svg>3 Ways to find the products. <u>Learn more</u><span class="x" style="margin-left:8px">✕</span></div>

    <span class="label" style="top:302px">Suggested</span>
    <div class="chips" style="top:328px"><span class="chip">All</span><span class="chip">Recommended</span><span class="chip">Favourit</span></div>
    <div class="chips" style="top:361px"><span class="chip">Discount</span><span class="chip">Price Drop</span><span class="chip">Cashback</span></div>
    <div class="chips" style="top:394px"><span class="chip">Rating</span><span class="chip">Popular</span><span class="chip more">···</span></div>

    <div class="retail">
      <span class="abs" style="left:18px;top:18px;font-size:14px;font-weight:500;color:var(--quarter)">Top Retailer</span>
      <span class="abs link" style="right:18px;top:18px;font-size:14px;font-style:italic">See all</span>
      <div class="tile" style="left:22px;top:42px"><i><em></em></i>Ambrola</div>
      <div class="tile" style="left:93px;top:42px"><i><em></em></i>Valtmo</div>
      <div class="tile" style="left:164px;top:42px"><i><em></em></i>Trendra</div>
      <div class="tile" style="left:236px;top:42px"><i><em></em></i>Zelimart</div>
      <div class="tile" style="left:22px;top:130px"><i></i>Retailer</div>
      <div class="tile" style="left:93px;top:130px"><i></i>Retailer</div>
      <div class="tile" style="left:164px;top:130px"><i></i>Retailer</div>
      <div class="tile" style="left:236px;top:130px"><i></i>Retailer</div>
    </div>

    <span class="abs" style="left:21px;top:686px;width:34px;height:34px;border-radius:6px;background:var(--secondary);color:var(--white);display:flex;align-items:center;justify-content:center"><svg class="ic" style="width:22px;height:22px;stroke-width:2.6"><use href="#i-search"/></svg></span>
    <span class="abs" style="left:62px;top:695px;font-size:13px">Result (80)</span>
    <span class="abs link" style="right:21px;top:687px;height:32px;padding:0 8px;border:1px solid var(--line);border-radius:8px;background:var(--white);display:flex;align-items:center;gap:6px;font-size:13px"><svg class="ic" style="width:16px;height:16px"><use href="#i-filter"/></svg>Filter</span>
    <div class="abs" style="left:21px;top:723px;width:323px;height:2px;background:var(--line)"></div>
    <span class="abs" style="left:21px;top:733px;width:70px;height:30px;border:1px solid var(--line);border-radius:8px;background:var(--white);display:flex;align-items:center;justify-content:center;gap:8px;font-size:13px;color:var(--muted)">Sort <svg class="ic" style="width:14px;height:14px;color:var(--secondary)"><use href="#i-down"/></svg></span>
    <span class="abs" style="right:108px;top:740px;font-size:14px">1/20</span>
    <span class="abs" style="right:21px;top:733px;width:82px;height:30px;border:1px solid var(--line);border-radius:15px;background:var(--white);display:flex;color:var(--secondary)"><span style="flex:1;display:flex;align-items:center;justify-content:center;border-right:1px solid var(--line)"><svg class="ic" style="width:14px;height:14px"><use href="#i-back"/></svg></span><span style="flex:1;display:flex;align-items:center;justify-content:center"><svg class="ic" style="width:14px;height:14px"><use href="#i-next"/></svg></span></span>

    <div class="vcard" style="left:22px;top:773px">
      <div class="ph ph-blue" role="img" aria-label="Yellow low sneaker product photo"><span class="check"></span><span class="off">50% OFF</span></div>
      <div class="info"><div class="pname">Yellow low sneakers</div><div class="rate"><b>★</b>4.8 <span>• 1028 sold</span></div><div class="brand" style="margin-top:8px">ambrola</div><div class="price">$37.50<small>$75.00</small></div><div class="acts" style="margin-top:6px"><span class="cmp">Compare</span><span class="add">Add <svg class="ic" style="width:14px;height:14px"><use href="#i-plus"/></svg></span></div></div>
    </div>
    <div class="vcard" style="left:190px;top:773px">
      <div class="ph ph-white" role="img" aria-label="Black high top sneaker product photo"><span class="check"></span><span class="off">50% OFF</span></div>
      <div class="info"><div class="pname">Yellow low sneakers</div><div class="rate"><b>★</b>4.8 <span>• 1028 sold</span></div><div class="brand" style="margin-top:8px">ambrola</div><div class="price">$37.50<small>$75.00</small></div><div class="acts" style="margin-top:6px"><span class="cmp">Compare</span><span class="add">Add <svg class="ic" style="width:14px;height:14px"><use href="#i-plus"/></svg></span></div></div>
    </div>
    <div class="vcard" style="left:22px;top:1082px">
      <div class="ph ph-dark" role="img" aria-label="Sunglasses on a blue stand product photo"><span class="check"></span><span class="off">50% OFF</span></div>
      <div class="info"><div class="pname">Yellow low sneakers</div><div class="rate"><b>★</b>4.8 <span>• 1028 sold</span></div><div class="brand" style="margin-top:8px">ambrola</div><div class="price">$37.50<small>$75.00</small></div><div class="acts" style="margin-top:6px"><span class="cmp">Compare</span><span class="add">Add <svg class="ic" style="width:14px;height:14px"><use href="#i-plus"/></svg></span></div></div>
    </div>
    <div class="vcard" style="left:188px;top:1082px">
      <div class="ph ph-steel" role="img" aria-label="White headphones product photo"><span class="check"></span><span class="off">50% OFF</span></div>
      <div class="info"><div class="pname">Yellow low sneakers</div><div class="rate"><b>★</b>4.8 <span>• 1028 sold</span></div><div class="brand" style="margin-top:8px">ambrola</div><div class="price">$37.50<small>$75.00</small></div><div class="acts" style="margin-top:6px"><span class="cmp">Compare</span><span class="add">Add <svg class="ic" style="width:14px;height:14px"><use href="#i-plus"/></svg></span></div></div>
    </div>

    <span class="abs" style="left:0;right:0;top:1390px;text-align:center;font-size:13px">1/20</span>
    <span class="abs" style="left:142px;top:1415px;width:82px;height:30px;border:1px solid var(--line);border-radius:15px;background:var(--white);display:flex;color:var(--secondary)"><span style="flex:1;display:flex;align-items:center;justify-content:center;border-right:1px solid var(--line)"><svg class="ic" style="width:14px;height:14px"><use href="#i-back"/></svg></span><span style="flex:1;display:flex;align-items:center;justify-content:center"><svg class="ic" style="width:14px;height:14px"><use href="#i-next"/></svg></span></span>

    <nav class="tabbar" style="top:1466px">
      <span class="tab"><svg><use href="#n-home"/></svg>Home</span>
      <span class="tab"><svg><use href="#n-globe"/></svg>Discover</span>
      <span class="tab"><svg><use href="#n-add"/></svg>Wishlist</span>
      <span class="tab"><svg><use href="#n-chat"/></svg>Chat</span>
      <span class="tab active"><svg><use href="#n-bag"/></svg>Shop</span>
    </nav>
  </section>
</main>
</body>
</html>
```